Banner Ad for Premium Supplement - RIVERS AWAKE

We need banner ads designed for our premium supplement, Rivers Awake.

Sizes to make (6): 125x125, 300x250, 240x400, 250x250, 160x600, 468x60

We sell mostly online via long form sales page. Here’s the link to our sales page:

https://shop.brivelgoods.example/tidalgreens

On that page you will see the product itself and some of our styling.

Our main website is here: http://www.brivelgoods.example/

Our style is best described as a harmony between science and nature:

Science = high tech, sophisticated, polished, professional, premium, clean, trustworthy

Nature = healthy, wholesome, nutritious, organic, full of life

Attached to this project is an RTF file with the verbiage for our ads. There are 2 versions. Please make 1 design for each size, in both versions (total of 12 designs).

```html
<!DOCTYPE html>
<html lang="en">
<head>
<meta charset="utf-8">
<title>Rivers Awake – Banner Set</title>
<link href="https://fonts.googleapis.com/css2?family=Fjalla+One&family=Source+Sans+3:wght@400;600;700&display=swap" rel="stylesheet">
<style>
:root{
  --sheet-bg:#141414;
  --sheet-bg-light:#262626;
  --label:#8d8d8d;
  --blue-light:#27b2ec;
  --blue-mid:#128fd6;
  --blue-deep:#0a63b3;
  --headline:#ffeb00;
  --copy:#ffffff;
  --divider:rgba(255,255,255,.35);
  --green:#5fae1f;
  --green-light:#9bd23c;
  --paper:#ffffff;
  --btn-top:#ffe566;
  --btn-bottom:#f6b800;
  --btn-text:#c4570a;
  --bottle-dark:#3a1f0c;
  --bottle-label:#2f8f2a;
}
*{margin:0;padding:0;box-sizing:border-box}
html,body{width:1200px;height:924px;overflow:hidden}
body{
  background:radial-gradient(ellipse at 50% 40%,var(--sheet-bg-light),var(--sheet-bg) 75%);
  font-family:"Source Sans 3",Arial,sans-serif;
}
.sheet{
  position:absolute;left:0;top:0;width:1069px;height:823px;
  transform:scale(1.1225);transform-origin:0 0;
}
.banner{
  position:absolute;overflow:hidden;
  background:linear-gradient(135deg,var(--blue-light) 0%,var(--blue-mid) 45%,var(--blue-deep) 100%);
  border:1px solid rgba(255,255,255,.6);
}
.banner > *{position:absolute}
.headline{
  font-family:"Fjalla One","Arial Narrow",sans-serif;
  color:var(--headline);white-space:nowrap;line-height:1;
  text-shadow:0 1px 2px rgba(0,0,0,.25);
}
.question{color:var(--copy);font-weight:700;line-height:1.18}
.pitch{color:var(--copy);font-weight:400;line-height:1.3}
.divider{height:1px;background:linear-gradient(90deg,transparent,var(--divider) 30%,var(--divider) 70%,transparent)}
.cta{
  display:flex;align-items:center;justify-content:center;
  background:linear-gradient(var(--btn-top),var(--btn-bottom));
  border-radius:4px;color:var(--btn-text);font-weight:400;
  box-shadow:0 2px 3px rgba(0,0,0,.3);white-space:nowrap;
}
.wordmark{color:var(--green);font-weight:600;line-height:1;white-space:nowrap;letter-spacing:.5px}
.bottles{
  border-radius:10px 10px 6px 6px;
  background:linear-gradient(180deg,var(--bottle-dark) 0%,var(--bottle-dark) 30%,var(--bottle-label) 50%,var(--bottle-label) 85%,var(--bottle-dark) 100%);
}
.swoosh{left:0;bottom:0;width:100%}
.size-label{position:absolute;color:var(--label);font-size:14px;font-weight:600;white-space:nowrap;line-height:1.3}
.sheet-mark{position:absolute;left:930px;top:770px;font-size:34px}
</style>
</head>
<body>
<div class="sheet">

  <!-- Leaderboard large -->
  <section class="banner" style="left:36px;top:19px;width:702px;height:89px">
    <svg class="swoosh" style="height:89px" viewBox="0 0 702 89" preserveAspectRatio="none" aria-hidden="true">
      <path d="M470 89 Q520 20 702 0 L702 89Z" fill="var(--green-light)"/>
      <path d="M490 89 Q540 26 702 8 L702 89Z" fill="var(--paper)"/>
    </svg>
    <div class="headline" style="left:8px;top:8px;font-size:30px">Did Yoy Know</div>
    <div class="question" style="left:8px;top:44px;font-size:16px;width:215px">100% of Life on Earth relies on&nbsp; ONE Superfood?</div>
    <div class="divider" style="left:222px;top:8px;width:1px;height:72px;background:var(--divider)"></div>
    <div class="pitch" style="left:230px;top:12px;font-size:13px;width:205px;line-height:1.25">See why &amp; how this little-known substance triggers your body to create TRILLIONS of healthy new cells!</div>
    <div class="bottles" role="img" aria-label="Dropper bottles of Rivers Awake supplement" style="left:448px;top:4px;width:44px;height:80px"></div>
    <div class="wordmark" style="left:516px;top:10px;font-size:40px">Brivel</div>
    <div class="cta" style="left:542px;top:54px;width:126px;height:28px;font-size:15px">CLICK HERE</div>
  </section>
  <div class="size-label" style="left:750px;top:54px">Size : 702px - 90px</div>

  <!-- Leaderboard small -->
  <section class="banner" style="left:36px;top:118px;width:468px;height:60px">
    <svg class="swoosh" style="height:60px" viewBox="0 0 468 60" preserveAspectRatio="none" aria-hidden="true">
      <path d="M320 60 Q350 12 468 0 L468 60Z" fill="var(--green-light)"/>
      <path d="M334 60 Q362 18 468 5 L468 60Z" fill="var(--paper)"/>
    </svg>
    <div class="headline" style="left:5px;top:4px;font-size:20px">Did Yoy Know</div>
    <div class="question" style="left:5px;top:30px;font-size:10px;width:145px">100% of Life on Earth relies on&nbsp; ONE Superfood?</div>
    <div class="divider" style="left:150px;top:4px;width:1px;height:52px;background:var(--divider)"></div>
    <div class="pitch" style="left:155px;top:3px;font-size:11.5px;width:175px;line-height:1.18">See why &amp; how this little-known substance triggers your body to create TRILLIONS of healthy new cells!</div>
    <div class="wordmark" style="left:350px;top:6px;font-size:26px">Brivel</div>
    <div class="cta" style="left:362px;top:36px;width:84px;height:18px;font-size:10px">CLICK HERE</div>
  </section>
  <div class="size-label" style="left:517px;top:139px">Size : 702px - 90px</div>

  <!-- Skyscraper 160x600 -->
  <section class="banner" style="left:36px;top:185px;width:160px;height:600px">
    <svg class="swoosh" style="height:90px" viewBox="0 0 100 100" preserveAspectRatio="none" aria-hidden="true">
      <path d="M0 30 Q50 45 100 0 L100 100 L0 100Z" fill="var(--green-light)"/>
      <path d="M0 40 Q50 54 100 10 L100 100 L0 100Z" fill="var(--paper)"/>
    </svg>
    <div class="headline" style="left:7px;top:20px;font-size:26px">Did Yoy Know</div>
    <div class="question" style="left:8px;top:56px;font-size:16.5px;width:128px;line-height:1.27">100% of Life on Earth relies on ONE Superfood?</div>
    <div class="divider" style="left:8px;top:134px;width:144px"></div>
    <div class="pitch" style="left:8px;top:145px;font-size:16px;width:148px;line-height:1.38">See why &amp; how this little-known substance triggers your body to create TRILLIONS of healthy new cells!</div>
    <div class="bottles" role="img" aria-label="Two dropper bottles of Rivers Awake supplement" style="left:38px;top:285px;width:96px;height:190px"></div>
    <div class="cta" style="left:24px;top:489px;width:112px;height:34px;font-size:15px">CLICK HERE</div>
    <div class="wordmark" style="left:20px;top:550px;font-size:36px">Brivel</div>
  </section>
  <div class="size-label" style="left:36px;top:788px">Size : 160px - 600px</div>

  <!-- 240x400 -->
  <section class="banner" style="left:211px;top:185px;width:240px;height:400px">
    <svg class="swoosh" style="height:95px" viewBox="0 0 100 100" preserveAspectRatio="none" aria-hidden="true">
      <path d="M0 22 Q50 40 100 0 L100 100 L0 100Z" fill="var(--green-light)"/>
      <path d="M0 30 Q50 48 100 8 L100 100 L0 100Z" fill="var(--paper)"/>
    </svg>
    <div class="headline" style="left:8px;top:17px;font-size:34px">Did Yoy Know</div>
    <div class="question" style="left:9px;top:59px;font-size:17px;width:228px;line-height:1.3">100% of Life on Earth relies on&nbsp; ONE Superfood?</div>
    <div class="divider" style="left:9px;top:118px;width:222px"></div>
    <div class="pitch" style="left:9px;top:133px;font-size:15.5px;width:215px;line-height:1.42">See why &amp; how this little-known substance triggers your body to create TRILLIONS of healthy new cells!</div>
    <div class="bottles" role="img" aria-label="Two dropper bottles of Rivers Awake supplement" style="left:158px;top:210px;width:80px;height:120px"></div>
    <div class="cta" style="left:9px;top:237px;width:125px;height:38px;font-size:16px">CLICK HERE</div>
    <div class="wordmark" style="left:62px;top:347px;font-size:42px">Brivel</div>
  </section>
  <div class="size-label" style="left:211px;top:590px">Size : 240px - 400px</div>

  <!-- 300x250 -->
  <section class="banner" style="left:464px;top:185px;width:300px;height:250px">
    <svg class="swoosh" style="height:70px" viewBox="0 0 100 100" preserveAspectRatio="none" aria-hidden="true">
      <path d="M0 20 Q50 35 100 0 L100 100 L0 100Z" fill="var(--green-light)"/>
      <path d="M0 30 Q50 45 100 10 L100 100 L0 100Z" fill="var(--paper)"/>
    </svg>
    <div class="headline" style="left:12px;top:15px;font-size:29px">Did Yoy Know</div>
    <div class="question" style="left:12px;top:52px;font-size:13.5px;width:182px">100% of Life on Earth relies on&nbsp; ONE Superfood?</div>
    <div class="divider" style="left:12px;top:94px;width:170px"></div>
    <div class="pitch" style="left:12px;top:106px;font-size:11px;width:182px;line-height:1.27">See why &amp; how this little-known substance triggers your body to create TRILLIONS of healthy new cells!</div>
    <div class="bottles" role="img" aria-label="Two dropper bottles of Rivers Awake supplement" style="left:198px;top:12px;width:94px;height:180px"></div>
    <div class="wordmark" style="left:30px;top:206px;font-size:34px">Brivel</div>
    <div class="cta" style="left:182px;top:210px;width:98px;height:30px;font-size:14px">CLICK HERE</div>
  </section>
  <div class="size-label" style="left:467px;top:438px">Size : 300px - 250px</div>

  <!-- 250x250 -->
  <section class="banner" style="left:784px;top:185px;width:250px;height:250px">
    <svg class="swoosh" style="height:70px" viewBox="0 0 100 100" preserveAspectRatio="none" aria-hidden="true">
      <path d="M0 20 Q50 35 100 0 L100 100 L0 100Z" fill="var(--green-light)"/>
      <path d="M0 30 Q50 45 100 10 L100 100 L0 100Z" fill="var(--paper)"/>
    </svg>
    <div class="headline" style="left:7px;top:8px;font-size:32px">Did Yoy Know</div>
    <div class="question" style="left:8px;top:46px;font-size:15px;width:215px;line-height:1.1">100% of Life on Earth relies on&nbsp; ONE Superfood?</div>
    <div class="divider" style="left:8px;top:86px;width:190px"></div>
    <div class="pitch" style="left:8px;top:95px;font-size:13px;width:200px;line-height:1.22">See why &amp; how this little-known substance triggers your body to create TRILLIONS of healthy new cells!</div>
    <div class="bottles" role="img" aria-label="Dropper bottle of Rivers Awake supplement" style="left:232px;top:68px;width:30px;height:176px"></div>
    <div class="cta" style="left:70px;top:165px;width:110px;height:32px;font-size:14px">CLICK HERE</div>
    <div class="wordmark" style="left:34px;top:206px;font-size:34px">Brivel</div>
  </section>
  <div class="size-label" style="left:780px;top:438px">Size : 250px - 250px</div>

  <!-- 336x280 -->
  <section class="banner" style="left:469px;top:487px;width:336px;height:280px">
    <svg class="swoosh" style="height:82px" viewBox="0 0 100 100" preserveAspectRatio="none" aria-hidden="true">
      <path d="M0 20 Q50 35 100 0 L100 100 L0 100Z" fill="var(--green-light)"/>
      <path d="M0 30 Q50 45 100 10 L100 100 L0 100Z" fill="var(--paper)"/>
    </svg>
    <div class="headline" style="left:13px;top:18px;font-size:33px">Did Yoy Know</div>
    <div class="question" style="left:13px;top:60px;font-size:15px;width:200px;line-height:1.3">100% of Life on Earth relies on&nbsp; ONE Superfood?</div>
    <div class="divider" style="left:13px;top:112px;width:190px"></div>
    <div class="pitch" style="left:13px;top:121px;font-size:13.5px;width:195px;line-height:1.2">See why &amp; how this little-known substance triggers your body to create TRILLIONS of healthy new cells!</div>
    <div class="bottles" role="img" aria-label="Two dropper bottles of Rivers Awake supplement" style="left:218px;top:16px;width:110px;height:192px"></div>
    <div class="wordmark" style="left:34px;top:230px;font-size:38px">Brivel</div>
    <div class="cta" style="left:195px;top:233px;width:125px;height:36px;font-size:16px">CLICK HERE</div>
  </section>
  <div class="size-label" style="left:469px;top:770px">Size : 336px - 280px</div>

  <!-- 125x125 -->
  <section class="banner" style="left:819px;top:487px;width:125px;height:125px">
    <svg class="swoosh" style="height:40px" viewBox="0 0 100 100" preserveAspectRatio="none" aria-hidden="true">
      <path d="M0 25 Q50 40 100 0 L100 100 L0 100Z" fill="var(--green-light)"/>
      <path d="M0 36 Q50 50 100 12 L100 100 L0 100Z" fill="var(--paper)"/>
    </svg>
    <div class="headline" style="left:5px;top:9px;font-size:18px">Did Yoy Know</div>
    <div class="question" style="left:0;top:33px;width:125px;font-size:12.5px;text-align:center;line-height:1.2">100% of Life on<br>Earth relies on<br>ONE Superfood?</div>
    <div class="wordmark" style="left:28px;top:97px;font-size:24px">Brivel</div>
  </section>
  <div class="size-label" style="left:815px;top:619px">Size : 125px - 125px<br>(this banner will make<br>in animation gif)</div>

  <div class="wordmark sheet-mark">Brivel</div>
</div>
</body>
</html>
```